VENTURE CAPITAL GROUP BUSINESS CARD DESIGN

Venture Capital Group based in SF looking for a bold business card design. No trendy colour explosion, 3D effects etc. Just "simple" optical effects. Works on your brain, keeps your eye focused and sticks to your mind.
Target Market(s)
Technology startups
Industry/Entity Type
Venture Capital
Contact Information for Business Card
BARNABY WHITLOCK
MANAGING PARTNER
817 FERN ST SAN FRANCISCO, CA 94111
415.555.0143 O
415.555.0167 F
415.555.0192 C
barn@halcyonridgefund.example

```html
<!DOCTYPE html>
<html lang="en">
<head>
<meta charset="utf-8">
<title>Halcyon Ridge Fund – Business Card</title>
<link rel="stylesheet" href="https://fonts.googleapis.com/css2?family=Source+Sans+3:wght@400;600&display=swap">
<style>
  :root {
    --backdrop-top: #2a2a2a;
    --backdrop-bottom: #050505;
    --card-light: #f2f2f2;
    --brand-green: #1e7d2a;
    --green-deep: #0d4a14;
    --green-mid: #2f8f35;
    --green-glow: #57b451;
    --ink: #1a1a1a;
    --white: #ffffff;
    --disc-light: #ffffff;
    --disc-shade: #d6d6d6;
  }
  * { box-sizing: border-box; margin: 0; padding: 0; }
  html, body { width: 1200px; height: 900px; overflow: hidden; }
  body {
    position: relative;
    background: linear-gradient(180deg, var(--backdrop-top) 0%, var(--backdrop-bottom) 100%);
    font-family: "Source Sans 3", "Myriad Pro", Arial, sans-serif;
  }
  .card {
    position: absolute;
    top: 184px;
    height: 490px;
    border-radius: 12px;
    box-shadow: 0 6px 18px rgba(0,0,0,0.55);
  }
  .card-front {
    left: 299px;
    width: 301px;
    background: var(--card-light);
    color: var(--ink);
    text-align: center;
  }
  .card-back {
    left: 645px;
    width: 304px;
    background: radial-gradient(ellipse 75% 60% at 48% 48%, var(--green-glow) 0%, var(--green-mid) 38%, var(--green-deep) 100%);
    color: var(--white);
    text-align: center;
  }
  .brand-disc {
    position: absolute;
    left: 95px;
    top: 30px;
    width: 112px;
    height: 112px;
    border-radius: 50%;
    background: radial-gradient(circle at 40% 35%, var(--disc-light) 0%, var(--disc-shade) 100%);
  }
  .brand-name {
    position: absolute;
    left: 0;
    width: 100%;
    font-weight: 600;
    color: var(--brand-green);
  }
  .brand-name .line-main { display: block; font-size: 31px; letter-spacing: 1px; line-height: 1; }
  .brand-name .line-sub { display: block; font-size: 10px; letter-spacing: 4px; margin-top: 4px; }
  .card-front .brand-name { top: 156px; }
  .card-back .brand-name { top: 350px; color: var(--white); }
  .holder {
    position: absolute;
    top: 265px;
    width: 100%;
  }
  .holder-name { font-size: 18px; font-weight: 600; color: var(--brand-green); line-height: 1.2; }
  .holder-title { font-size: 13px; line-height: 1.4; }
  .contact {
    position: absolute;
    top: 348px;
    width: 100%;
    list-style: none;
    font-size: 13px;
    line-height: 20.5px;
  }
  .contact li { display: flex; justify-content: center; align-items: center; gap: 5px; }
  .contact svg { width: 9px; height: 9px; fill: var(--brand-green); flex: none; }
  .address {
    position: absolute;
    top: 438px;
    width: 100%;
    font-size: 13px;
  }
</style>
</head>
<body>
  <section class="card card-front" aria-label="Card front">
    <div class="brand-disc"></div>
    <div class="brand-name">
      <span class="line-main">HALCYON</span>
      <span class="line-sub">RIDGE FUND</span>
    </div>
    <div class="holder">
      <p class="holder-name">Barnaby Whitlock</p>
      <p class="holder-title">Managing Partner</p>
    </div>
    <ul class="contact">
      <li><svg viewBox="0 0 10 10" aria-hidden="true"><path d="M2 0.5 L3.6 2.6 L2.7 3.7 C3.4 5.2 4.8 6.6 6.3 7.3 L7.4 6.4 L9.5 8 L8.5 9.5 C4.5 9.2 0.8 5.5 0.5 1.5 Z"/></svg>415.555.0143</li>
      <li><svg viewBox="0 0 10 10" aria-hidden="true"><path d="M0.5 3 H9.5 V9 H0.5 Z M2.5 0.5 H7.5 V3 H2.5 Z"/></svg>415.555.0167</li>
      <li><svg viewBox="0 0 10 10" aria-hidden="true"><path d="M2.5 0 H7.5 V10 H2.5 Z M3.3 1 V8 H6.7 V1 Z"/></svg>415.555.0192</li>
      <li><svg viewBox="0 0 10 10" aria-hidden="true"><path d="M0.5 2 H9.5 V8.5 H0.5 Z M0.5 2 L5 5.5 L9.5 2" /></svg>barn@halcyonridgefund.example</li>
    </ul>
    <p class="address">817 Fern St San Francisco, CA 94111</p>
  </section>

  <section class="card card-back" aria-label="Card back">
    <div class="brand-name">
      <span class="line-main">HALCYON</span>
      <span class="line-sub">RIDGE FUND</span>
    </div>
  </section>
</body>
</html>
```